Kai & Palz

I am looking for help designing a concert benefit flyer. I recently designed a ticket for the event. Attached is the font and the back.
The event is being thrown for Kai Bennett Lo'o Lo'o Haver – He is IMAGE 5112 / 5113/5110 ( I have uploaded 3 options – just use the best that you think would work)
We have 7 different artist’s who will be showcased in the event that we would like to incorporate in the flyer
Image 5107 is the main Artist
“ Buro and the list below is his Palz”
Image 5101 is “Pualu”
Image 5102 is Tobin Garcela
Image 5103 is Ikaika Lopes
Image 5104 is Marisa Dutra
Image 5106 is Ilima Segundo
Image 5109 is “Manuheali”
I have uploaded an old flyer we created for a smaller event and was wondering if you could help us design this one ?
Please let me know if you can help and I will go into further details?
Corinne Talua
HALEWAI MANAGEMENT

```html
<!DOCTYPE html>
<html lang="en">
<head>
<meta charset="utf-8">
<title>Kai &amp; Palz – Benefit Concert</title>
<link rel="stylesheet" href="https://fonts.googleapis.com/css2?family=Cormorant+Garamond:ital,wght@1,600&family=Montserrat:wght@600;700;800&family=Oswald:wght@500&display=swap">
<style>
  :root {
    --charcoal: #262626;
    --black: #0b0b0b;
    --gold: #f4c21b;
    --white: #ffffff;
    --chevron: #9a9a9a;
    --bars: #bdbdbd;
  }
  html, body { margin: 0; padding: 0; overflow: hidden; background: var(--black); }
  .flyer {
    position: relative;
    width: 848px;
    height: 1200px;
    overflow: hidden;
    background: var(--charcoal);
    font-family: "Montserrat", sans-serif;
    color: var(--white);
  }
  .backdrop, .chevrons, .equalizer, .recipient-photo, .divider {
    position: absolute; left: 0; top: 0;
  }
  .title {
    position: absolute; top: 12px; left: 0; width: 100%;
    margin: 0; text-align: center;
    font-family: "Cormorant Garamond", serif;
    font-style: italic; font-weight: 600;
    font-size: 72px; letter-spacing: 1px; color: var(--white);
  }
  .recipient-label {
    position: absolute; top: 200px; left: 74px; width: 342px;
    text-align: center; font-weight: 700; font-size: 21px; color: var(--gold);
  }
  .headline {
    position: absolute; top: 156px; left: 480px; width: 340px; margin: 0;
    font-family: "Oswald", sans-serif; font-weight: 500;
    font-size: 18px; line-height: 34px; color: var(--gold); text-transform: uppercase;
  }
  .lineup-note {
    position: absolute; top: 258px; left: 480px; width: 340px; margin: 0;
    font-weight: 700; font-size: 15px; line-height: 23px; color: var(--white);
  }
  .purpose {
    position: absolute; top: 404px; left: 480px; width: 300px; margin: 0;
    font-family: "Oswald", sans-serif; font-weight: 500;
    font-size: 13.5px; line-height: 24px; color: var(--gold); text-transform: uppercase;
  }
  .artist {
    position: absolute; top: 762px; width: 87px; height: 87px;
    border-radius: 50%; border: 3px solid var(--gold); overflow: hidden;
  }
  .artist-photo { width: 100%; height: 100%; }
  .artist-mark { background: #8b2323; }
  .artist-names {
    position: absolute; top: 870px; left: 0; width: 848px; margin: 0;
    text-align: center; font-weight: 700; font-size: 16px; color: var(--gold); word-spacing: 2px;
  }
  .organizer {
    position: absolute; top: 898px; left: 0; width: 848px; margin: 0;
    text-align: center; font-weight: 800; font-size: 15px; color: var(--white);
  }
  .host-portrait {
    position: absolute; top: 896px; left: 64px; width: 100px; height: 100px;
    border-radius: 50%; border: 3px solid var(--gold); overflow: hidden;
  }
  .details {
    position: absolute; top: 980px; left: 170px; width: 640px; text-align: center;
  }
  .invite { margin: 0 0 28px; font-weight: 800; font-size: 23px; color: var(--gold); }
  .date { margin: 0; font-weight: 700; font-size: 21px; color: var(--gold); }
  .venue { margin: 4px 0 0; font-weight: 700; font-size: 20px; color: var(--white); }
  .entry { margin: 8px 0 0; font-weight: 700; font-size: 15px; color: var(--white); }
</style>
</head>
<body>
<main class="flyer">
  <svg class="backdrop" width="848" height="1200" aria-hidden="true">
    <polygon points="0,456 848,712 848,1200 0,1200" fill="var(--black)"/>
  </svg>

  <h1 class="title">Kai &amp; Palz</h1>

  <svg class="recipient-photo" width="848" height="760" role="img" aria-label="Photo of benefit recipient Kai Bennett Lo'o Lo'o Haver in a flat cap before a mountain canyon">
    <defs>
      <linearGradient id="photoTones" x1="0" y1="0" x2="0" y2="1">
        <stop offset="0" stop-color="#3b78c2"/>
        <stop offset="0.35" stop-color="#8fb2d4"/>
        <stop offset="0.55" stop-color="#7d6a55"/>
        <stop offset="1" stop-color="#9a9a98"/>
      </linearGradient>
    </defs>
    <path fill="url(#photoTones)" d="M74 176 L88 166 L100 178 L114 162 L128 174 L142 164 L156 178 L170 160 L186 172 L200 164 L214 178 L230 162 L246 174 L260 166 L276 178 L290 160 L306 172 L320 164 L334 176 L350 162 L364 174 L378 166 L392 178 L404 164 L416 172
      L416 668 L402 680 L388 664 L372 678 L358 668 L342 684 L328 670 L312 680 L298 664 L282 678 L268 668 L252 682 L238 666 L222 678 L208 668 L192 684 L178 670 L162 680 L148 666 L132 678 L118 668 L104 682 L90 668 L74 678 Z"/>
  </svg>
  <div class="recipient-label">Benefit Recipient</div>

  <p class="headline">A benefit concert for Kai Bennett<br>Lo'o Lo'o Haver</p>
  <p class="lineup-note">Live Hawaiian Music, Entertainment by the "Sunday Sisters" and Live Raffle Giveaway!</p>
  <p class="purpose">All ticket sales will go towards Kai's<br>medical expenses</p>

  <svg class="chevrons" width="848" height="760" aria-hidden="true">
    <g fill="var(--chevron)">
      <polygon points="552,598 605,470 635,470 582,598 635,727 605,727"/>
      <polygon points="622,598 675,470 705,470 652,598 705,727 675,727"/>
      <polygon points="692,598 745,470 775,470 722,598 775,727 745,727"/>
    </g>
  </svg>

  <svg class="equalizer" width="848" height="760" aria-hidden="true">
    <defs>
      <pattern id="barSegments" width="8" height="5" patternUnits="userSpaceOnUse">
        <rect width="8" height="3.5" fill="var(--bars)"/>
      </pattern>
    </defs>
    <g fill="url(#barSegments)">
      <rect x="85" y="730" width="6" height="18"/><rect x="93" y="712" width="6" height="36"/>
      <rect x="101" y="694" width="6" height="54"/><rect x="109" y="704" width="6" height="44"/>
      <rect x="117" y="720" width="6" height="28"/><rect x="125" y="732" width="6" height="16"/>
      <rect x="145" y="726" width="6" height="22"/><rect x="153" y="710" width="6" height="38"/>
      <rect x="161" y="722" width="6" height="26"/><rect x="169" y="734" width="6" height="14"/>
      <rect x="189" y="716" width="6" height="32"/><rect x="197" y="700" width="6" height="48"/>
      <rect x="205" y="686" width="6" height="62"/><rect x="213" y="696" width="6" height="52"/>
      <rect x="221" y="714" width="6" height="34"/><rect x="229" y="730" width="6" height="18"/>
      <rect x="249" y="732" width="6" height="16"/><rect x="257" y="718" width="6" height="30"/>
      <rect x="265" y="728" width="6" height="20"/>
      <rect x="293" y="712" width="6" height="36"/><rect x="301" y="698" width="6" height="50"/>
      <rect x="309" y="708" width="6" height="40"/><rect x="317" y="690" width="6" height="58"/>
      <rect x="325" y="704" width="6" height="44"/><rect x="333" y="718" width="6" height="30"/>
      <rect x="341" y="732" width="6" height="16"/>
      <rect x="361" y="722" width="6" height="26"/><rect x="369" y="708" width="6" height="40"/>
      <rect x="377" y="720" width="6" height="28"/>
      <rect x="403" y="726" width="6" height="22"/><rect x="411" y="714" width="6" height="34"/>
      <rect x="419" y="702" width="6" height="46"/><rect x="427" y="716" width="6" height="32"/>
      <rect x="435" y="730" width="6" height="18"/>
      <rect x="469" y="730" width="6" height="18"/><rect x="477" y="712" width="6" height="36"/>
      <rect x="485" y="722" width="6" height="26"/>
      <rect x="511" y="700" width="6" height="48"/><rect x="519" y="686" width="6" height="62"/>
      <rect x="527" y="698" width="6" height="50"/><rect x="535" y="714" width="6" height="34"/>
      <rect x="555" y="724" width="6" height="24"/><rect x="563" y="712" width="6" height="36"/>
      <rect x="571" y="728" width="6" height="20"/>
    </g>
    <rect x="67" y="750" width="510" height="2" fill="var(--white)"/>
  </svg>

  <div class="artist artist-mark" style="left:70px" role="img" aria-label="Manuheali artist mark"></div>
  <div class="artist" style="left:173px"><svg class="artist-photo" viewBox="0 0 10 10" role="img" aria-label="Portrait of Pualu"><rect width="10" height="10" fill="#b08a62"/></svg></div>
  <div class="artist" style="left:281px"><svg class="artist-photo" viewBox="0 0 10 10" role="img" aria-label="Portrait of Marisa Dutra"><rect width="10" height="10" fill="#9ec3d6"/></svg></div>
  <div class="artist" style="left:384px"><svg class="artist-photo" viewBox="0 0 10 10" role="img" aria-label="Portrait of Ilima Segundo"><rect width="10" height="10" fill="#6b4a3c"/></svg></div>
  <div class="artist" style="left:486px"><svg class="artist-photo" viewBox="0 0 10 10" role="img" aria-label="Portrait of Tobin Garcela"><rect width="10" height="10" fill="#4f6a5a"/></svg></div>
  <div class="artist" style="left:589px"><svg class="artist-photo" viewBox="0 0 10 10" role="img" aria-label="Portrait of Ikaika Lopes"><rect width="10" height="10" fill="#7a5840"/></svg></div>
  <div class="artist" style="left:691px"><svg class="artist-photo" viewBox="0 0 10 10" role="img" aria-label="Portrait of Nalu Kahale"><rect width="10" height="10" fill="#7f95a8"/></svg></div>

  <p class="artist-names">Manuheali &nbsp;-&nbsp; Pualu &nbsp;-&nbsp; Marisa &nbsp;-&nbsp; Ilima &nbsp;-&nbsp; Tobin &nbsp;-&nbsp; Ikaika Lopes &nbsp;-&nbsp; Nalu Kahale</p>
  <p class="organizer">EVENT BY HALEWAI MANAGEMENT GROUP</p>

  <svg class="divider" width="848" height="960" aria-hidden="true">
    <rect x="100" y="934" width="748" height="4" fill="var(--gold)"/>
  </svg>
  <div class="host-portrait"><svg class="artist-photo" viewBox="0 0 10 10" role="img" aria-label="Portrait of main artist Buro"><rect width="10" height="10" fill="#a7a196"/></svg></div>

  <section class="details">
    <p class="invite">Please Join Us For Dinner &amp; Live Music</p>
    <p class="date">March 9th, 2024 from 4pm - 8pm</p>
    <p class="venue">at the Moana Bay Lu'au Pavillion</p>
    <p class="entry">Ticketed Entry Only</p>
  </section>
</main>
</body>
</html>
```